Ask Skybox Grows up and Wordpress website

We need a Wordpress theme design for Ask Skybox. Ask Skybox is a training site for people who don't know how to use Pearwell's Skyvault. We have already had a brand created and now would like that applied to a website.
A website that is easy and simple to use, that enables video viewing for public and paid subscriptions is ideal.
Updates

Project Deadline Extended
Reason: I am waiting on a design from someone who has yet to submit.

Target Market(s)

Mums with Pocketels, generally a female audience

Industry/Entity Type

Training

Coding

Coded - Design and coding required

Number of Pages Required

3 page

Font styles to use
Sans Serif

Colors
33a6d7
f04a50

Requirements
Must have
• Must have a section for a Jargon Buster (like an FAQ)
• Blog page
• Video feeds from Youtube or other hosting service
Nice to have
• Feeds from Social Media
• Login for Subscription to videos and other services
Should not have
• Complicated language

```html
<!DOCTYPE html>
<html lang="en">
<head>
<meta charset="utf-8">
<title>Ask Skybox – Home</title>
<link href="https://fonts.googleapis.com/css2?family=Montserrat:wght@400;600;700&family=Open+Sans:ital,wght@0,400;0,600;1,600&display=swap" rel="stylesheet">
<style>
:root{
  --blue:#33a6d7;
  --red:#f04a50;
  --teal:#1a9a8c;
  --yellow:#f2c21a;
  --ink:#333;
  --muted:#555;
  --mist:#eef1f4;
  --icon-bg:#eef0f1;
  --footer:#3b3b3b;
  --white:#fff;
}
*{box-sizing:border-box;margin:0;padding:0}
html,body{width:1200px;height:1200px;overflow:hidden;background:var(--white)}
body{font-family:"Open Sans",Arial,sans-serif;color:var(--ink);position:relative}
.page{position:absolute;left:395px;top:0;width:410px;height:1200px;overflow:hidden}
section,header,footer{position:relative;width:410px}
.abs{position:absolute}
.center{left:0;right:0;text-align:center}
h1,h2,h3,h4{font-family:"Montserrat",Arial,sans-serif;letter-spacing:.06em}
p{letter-spacing:.05em}
.btn{position:absolute;height:19px;width:97px;font:600 6.4px/19px "Montserrat",Arial,sans-serif;letter-spacing:.08em;color:var(--white);text-align:center}
.btn--blue{background:var(--blue)}
.btn--red{background:var(--red)}
.lede{font-size:4.8px;line-height:8.2px;color:var(--muted)}

/* header */
.site-header{height:31px;border-bottom:1px solid #ccc;background:var(--white)}
.brand{left:30px;top:8px;display:flex;align-items:center;gap:5px}
.brand__dot{width:14px;height:14px;border-radius:50%;background:var(--blue)}
.brand__name{font:600 10px "Montserrat",Arial,sans-serif;color:var(--blue);letter-spacing:.02em}
.nav{left:146px;top:12px;display:flex;gap:9px;font:600 4.8px "Montserrat",Arial,sans-serif;color:var(--ink)}
.login{left:346px;top:12px;font:600 4.8px "Montserrat",Arial,sans-serif;color:var(--red)}
.search{left:375px;top:11px}

/* hero */
.hero{height:181px}
.hero__photo{position:absolute;inset:0;background:linear-gradient(90deg,#3c3d3b 0%,#4a5446 35%,#7d8a6c 55%,#c9b7b2 72%,#dfe3e4 100%)}
.hero__title{left:30px;top:37px;color:var(--white);font-size:15px;line-height:18.5px;font-weight:600}
.hero__text{left:30px;top:79px;width:175px;color:var(--white);font-size:5.6px;line-height:9px;font-weight:400}
.hero .btn{left:30px;top:113px}
.band{height:14px;background:var(--blue);color:var(--white);font-size:4.4px;line-height:14px;text-align:center;letter-spacing:.05em}

/* steps */
.steps{height:132px;background:var(--red)}
.steps h2{top:23px;color:var(--white);font-size:10px;font-weight:600}
.step{position:absolute;top:53px;width:113px;height:54px;background:#f2f2f2;display:flex;align-items:center;padding-left:4px}
.step__num{width:32px;height:32px;border-radius:50%;background:var(--red);color:var(--white);font:600 15px/32px "Montserrat",Arial,sans-serif;text-align:center;flex:none}
.step__body{margin-left:6px}
.step h3{color:var(--red);font-size:7px;font-weight:600;margin-bottom:2px}
.step p{font-size:4px;line-height:7px;color:var(--muted)}

/* supported */
.supported{height:253px;background:linear-gradient(180deg,#5b9ad8 0%,#2f7ed2 30%,#5a8bb5 60%,#b08158 85%,#b8733e 100%)}
.supported h2{top:24px;color:var(--white);font-size:10px;font-weight:600}
.supported .lede{top:42px;color:var(--white)}
.supported .btn{left:157px;top:74px}
.devices{position:absolute;left:78px;top:102px;width:253px;height:136px;border-radius:6px;background:linear-gradient(135deg,#2a2a2e 0%,#55576a 50%,#c7c9d4 100%)}

/* features */
.features{height:232px}
.features h2{top:19px;color:var(--blue);font-size:10px;font-weight:600}
.features .lede{top:37px}
.feature{position:absolute;top:74px;width:84px;text-align:center}
.feature__icon{width:32px;height:32px;border-radius:50%;background:var(--icon-bg);margin:0 auto;display:flex;align-items:center;justify-content:center}
.feature h3{font-size:7px;font-weight:600;margin-top:12px}
.feature p{font-size:4.5px;line-height:7.8px;color:var(--muted);margin-top:5px}
.features .btn{left:157px;top:187px}
.fineprint{top:211px;font-size:4px;color:var(--muted)}

/* testimonial */
.testimonial{height:119px;background:var(--mist)}
.quote-mark{top:16px;font:700 18px Georgia,serif;color:#9aa3ad}
.testimonial p{top:54px;font-size:6px;line-height:8.5px;color:var(--muted)}
.author{top:89px;font:italic 600 5.6px "Open Sans",Arial,sans-serif;letter-spacing:.06em;color:var(--ink)}
.arrow{top:53px}

/* blog */
.blog{height:212px}
.blog h2{top:17px;color:var(--blue);font-size:10.5px;font-weight:600}
.blog .lede{top:36px}
.post{position:absolute;top:78px;width:113px;height:122px;background:var(--red);padding:3px}
.post__image{height:54px;background:linear-gradient(135deg,#6a4fc9 0%,#4fa5e6 50%,#f3a24f 100%)}
.post h3{color:var(--white);font-size:7px;font-weight:600;margin:5px 0 3px 1px}
.post p{color:var(--white);font-size:4.2px;line-height:7.2px;margin-left:1px}
.post__more{display:inline-block;margin:3px 0 0 1px;background:var(--blue);color:var(--white);font:600 4.6px/12px "Montserrat",Arial,sans-serif;padding:0 8px;letter-spacing:.06em}

/* footer */
.site-footer{height:26px;background:var(--footer)}
.copyright{left:30px;top:10px;color:#ddd;font-size:4.4px;letter-spacing:.05em}
.social{right:30px;top:6px;display:flex;gap:4px}
.social span{width:14px;height:14px;background:#e6e6e6}
</style>
</head>
<body>
<main class="page">

  <header class="site-header">
    <div class="abs brand"><span class="brand__dot"></span><span class="brand__name">Ask Skybox</span></div>
    <nav class="abs nav"><span>Home</span><span>Jargon baster</span><span>Videos</span><span>Pricing</span></nav>
    <span class="abs login">Login</span>
    <svg class="abs search" width="6" height="6" viewBox="0 0 10 10"><circle cx="4" cy="4" r="3" fill="none" stroke="#f04a50" stroke-width="1.5"/><line x1="6.2" y1="6.2" x2="9.5" y2="9.5" stroke="#f04a50" stroke-width="1.5"/></svg>
  </header>

  <section class="hero">
    <div class="hero__photo" role="img" aria-label="Photo of a smiling woman on the phone working at a laptop in a bright office with plants"></div>
    <h1 class="abs hero__title">Enterprise Endpoint<br>Backup &amp; Restore</h1>
    <p class="abs hero__text">Lorem Ipsum is simply dummy text of the printing<br>and typesetting industry. Lorem Ipsum has been the<br>industry's standard dummy.</p>
    <span class="btn btn--blue">Get Started It's Free</span>
  </section>
  <div class="band">Lorem ipsum lorem ipsum lorem ipsum lorem ipsum From Hackers</div>

  <section class="steps">
    <h2 class="abs center">Lorem Ipsum Lorem Ipsum.</h2>
    <div class="step" style="left:29px"><span class="step__num">1</span><div class="step__body"><h3>Lorem</h3><p>Lorem Ipsum is simply dummy<br>text of the printing and<br>typesetting industry.</p></div></div>
    <div class="step" style="left:148px"><span class="step__num">2</span><div class="step__body"><h3>Lorem</h3><p>Lorem Ipsum is simply dummy<br>text of the printing and<br>typesetting industry.</p></div></div>
    <div class="step" style="left:268px"><span class="step__num">3</span><div class="step__body"><h3>Lorem</h3><p>Lorem Ipsum is simply dummy<br>text of the printing and<br>typesetting industry.</p></div></div>
  </section>

  <section class="supported">
    <h2 class="abs center">Skyvault Supported</h2>
    <p class="abs center lede">Lorem Ipsum is simply dummy text of the printing and typesetting industry.<br>Lorem Ipsum has been the industry's standard dummy text<br>ever since the 1500s</p>
    <span class="btn btn--red">Get Started It's Free</span>
    <div class="devices" role="img" aria-label="Laptop, tablet and phone showing a photo library in the cloud"></div>
  </section>

  <section class="features">
    <h2 class="abs center">Lorem Ipsum Lorem.</h2>
    <p class="abs center lede">Lorem Ipsum is simply dummy text of the printing and typesetting industry.<br>Lorem Ipsum has been the industry's standard dummy text<br>ever since the 1500s</p>

    <div class="feature" style="left:29px">
      <div class="feature__icon"><svg width="16" height="16" viewBox="0 0 16 16"><path d="M4.5 5a5 5 0 1 1-1 4.5" fill="none" stroke="#1a9a8c" stroke-width="1.6" stroke-linecap="round"/><path d="M2.5 2.5v3.5h3.5" fill="none" stroke="#1a9a8c" stroke-width="1.6" stroke-linecap="round" stroke-linejoin="round"/></svg></div>
      <h3 style="color:var(--teal)">Smart Backup</h3>
      <p>Lorem Ipsum is simply dummy text of the printing and typesetting industry. Lorem Ipsum has been the industry's standard dummy text ever since the 1500s.</p>
    </div>
    <div class="feature" style="left:118px">
      <div class="feature__icon"><svg width="16" height="16" viewBox="0 0 16 16"><path d="M3 13l1-3.5 7-7 2.5 2.5-7 7z" fill="none" stroke="#f2c21a" stroke-width="1.5" stroke-linejoin="round"/><line x1="9.5" y1="4" x2="12" y2="6.5" stroke="#f2c21a" stroke-width="1.5"/></svg></div>
      <h3 style="color:var(--yellow)">Notes</h3>
      <p>Lorem Ipsum is simply dummy text of the printing and typesetting industry. Lorem Ipsum has been the industry's standard dummy text ever since the 1500s.</p>
    </div>
    <div class="feature" style="left:207px">
      <div class="feature__icon"><svg width="16" height="16" viewBox="0 0 16 16"><path d="M5 7V5a3 3 0 0 1 6 0v2" fill="none" stroke="#1e8ef0" stroke-width="1.6"/><rect x="3.5" y="7" width="9" height="7" rx="1" fill="#1e8ef0"/></svg></div>
      <h3 style="color:var(--blue)">Data Security</h3>
      <p>Lorem Ipsum is simply dummy text of the printing and typesetting industry. Lorem Ipsum has been the industry's standard dummy text ever since the 1500s.</p>
    </div>
    <div class="feature" style="left:296px">
      <div class="feature__icon"><svg width="20" height="10" viewBox="0 0 20 10"><path d="M10 5C8 2 6 1.5 4.5 1.5a3.5 3.5 0 0 0 0 7C6 8.5 8 8 10 5s4-3.5 5.5-3.5a3.5 3.5 0 0 1 0 7C14 8.5 12 8 10 5z" fill="none" stroke="#111" stroke-width="1.6"/></svg></div>
      <h3 style="color:#111">Unlimited Storage</h3>
      <p>Lorem Ipsum is simply dummy text of the printing and typesetting industry. Lorem Ipsum has been the industry's standard dummy text ever since the 1500s.</p>
    </div>

    <span class="btn btn--blue">Get Started It's Free</span>
    <p class="abs center fineprint">No credit card required</p>
  </section>

  <section class="testimonial">
    <div class="abs center quote-mark">&ldquo;</div>
    <svg class="abs arrow" style="left:35px" width="8" height="14" viewBox="0 0 8 14"><path d="M7 1L1 7l6 6" fill="none" stroke="#c3c9cf" stroke-width="1.2"/></svg>
    <p class="abs center">Lorem Ipsum is simply dummy text of the printing and typesetting industry.<br>Lorem Ipsum has been the industry's standard dummy</p>
    <div class="abs center author">Mara Quill, Lodon</div>
    <svg class="abs arrow" style="left:367px" width="8" height="14" viewBox="0 0 8 14"><path d="M1 1l6 6-6 6" fill="none" stroke="#c3c9cf" stroke-width="1.2"/></svg>
  </section>

  <section class="blog">
    <h2 class="abs center">Our Blog</h2>
    <p class="abs center lede">Lorem Ipsum is simply dummy text of the printing and typesetting industry.<br>Lorem Ipsum has been the industry's standard dummy text<br>ever since the 1500s</p>
    <article class="post" style="left:29px">
      <div class="post__image" role="img" aria-label="Illustration of a cloud with app icons rising from a laptop"></div>
      <h3>Lorem Ipsum Lorem</h3>
      <p>Lorem Ipsum is simply dummy text of the printing and typesetting industry. Lorem Ipsum has been the industry's standard dummy text ever since the 1500s.</p>
      <span class="post__more">Lean More..</span>
    </article>
    <article class="post" style="left:148px">
      <div class="post__image" role="img" aria-label="Illustration of a cloud with app icons rising from a laptop"></div>
      <h3>Lorem Ipsum Lorem</h3>
      <p>Lorem Ipsum is simply dummy text of the printing and typesetting industry. Lorem Ipsum has been the industry's standard dummy text ever since the 1500s.</p>
      <span class="post__more">Lean More..</span>
    </article>
    <article class="post" style="left:268px">
      <div class="post__image" role="img" aria-label="Illustration of a cloud with app icons rising from a laptop"></div>
      <h3>Lorem Ipsum Lorem</h3>
      <p>Lorem Ipsum is simply dummy text of the printing and typesetting industry. Lorem Ipsum has been the industry's standard dummy text ever since the 1500s.</p>
      <span class="post__more">Lean More..</span>
    </article>
  </section>

  <footer class="site-footer">
    <p class="abs copyright">&copy; Copyright www.example.com All Right Reserved</p>
    <div class="abs social" aria-label="Social links"><span></span><span></span><span></span><span></span></div>
  </footer>

</main>
</body>
</html>
```